Physical Therapy Center for children Business Card

We need a Business Card for our company (Physical Therapy for children and youth with special needs) in Lisbon, Portugal. The name of the company is "Ninho de Luz"

The card must contain the following info:
- Logo: see uploaded file
- Name: Ninho de Luz
- Slogan: Plantamos carinho, cuidamos sorrisos, celebramos conquistas!
- Service: Terapias Especializadas
- Address: Rua Henrique Lobato Farinha 9C
- ZipCode: 2741-318 Quinta do Orvalho
- E-mail: geral@velado.pt
- Site: www.velado.pt
- Facebook: www.facebook.com/ninhodeluz
- Phone: +351 21 584 62 07
- Cell Phone: +351 96 731 84 25

The stationary should have contain all info from business card.

Target Market(s)

Parents of children with special needs

Industry/Entity Type

Physical Therapy

Contact Information for Business Card

The card design should be compatible with http://www.quellprensa.com/product2/order_detail.php?gid=40

Requirements
Should not have
• The business card should not have a Black background. Use white or other color.

```html
<!DOCTYPE html>
<html lang="pt">
<head>
<meta charset="utf-8">
<title>Ninho de Luz — Cartão de Visita</title>
<link href="https://fonts.googleapis.com/css2?family=Fira+Sans+Condensed:wght@600&family=Open+Sans:ital,wght@0,400;0,600;1,400&display=swap" rel="stylesheet">
<style>
  :root{
    --bg:#e9e9eb;
    --white:#ffffff;
    --grey:#8a8a8c;
    --grey-text:#f2f2f2;
    --name-grey:#6f6f72;
    --teal:#2bb09c;
    --yellow:#f3c933;
    --red:#e4574f;
    --purple:#7a4f8e;
    --brand-grey:#8c8c8e;
  }
  *{margin:0;padding:0;box-sizing:border-box}
  html,body{width:1200px;height:950px;overflow:hidden;background:var(--bg)}
  body{font-family:"Open Sans",Arial,sans-serif;position:relative}

  .card{position:absolute;left:250px;width:700px;height:400px;overflow:hidden;
        box-shadow:0 4px 14px rgba(0,0,0,.18)}
  .card--front{top:50px;background:var(--white)}
  .card--back{top:500px;background:var(--teal)}

  /* front */
  .front__top{position:absolute;left:0;top:0;width:100%;height:218px;background:var(--white)}
  .front__stripe{position:absolute;left:0;top:218px;width:100%;height:6px;display:flex}
  .front__stripe span{flex:1}
  .front__stripe .s-teal{background:var(--teal)}
  .front__stripe .s-yellow{background:var(--yellow)}
  .front__stripe .s-red{background:var(--red)}
  .front__stripe .s-purple{background:var(--purple)}
  .front__bottom{position:absolute;left:0;top:224px;width:100%;height:176px;background:var(--grey)}

  .brand{position:absolute;left:50px;top:140px;display:flex;align-items:center;gap:14px}
  .brand__dot{width:34px;height:34px;border-radius:50%;background:var(--teal)}
  .brand__name{font-family:"Fira Sans Condensed",Arial,sans-serif;font-weight:600;font-size:36px;color:var(--brand-grey)}

  .person{position:absolute;right:46px;top:40px;text-align:right}
  .person__name{font-size:26px;color:var(--name-grey);font-weight:400}
  .person__role{font-size:17px;color:var(--teal);margin-top:2px}

  .contacts{position:absolute;left:50px;top:28px;list-style:none}
  .contacts li{display:flex;align-items:center;gap:12px;color:var(--grey-text);font-size:17px;line-height:25px}
  .contacts svg{width:16px;height:16px;flex:none}

  .address{position:absolute;right:46px;top:28px;text-align:right;color:var(--grey-text);font-size:17px;line-height:25px}

  /* back */
  .back__brand{position:absolute;left:0;right:0;top:120px;display:flex;flex-direction:column;align-items:center;gap:16px}
  .back__dot{width:70px;height:70px;border-radius:50%;background:var(--white)}
  .back__name{font-family:"Fira Sans Condensed",Arial,sans-serif;font-weight:600;font-size:44px;color:var(--white)}
  .slogan{position:absolute;left:0;right:0;bottom:70px;text-align:center;color:var(--white);font-size:18px;font-style:italic}
</style>
</head>
<body>

<section class="card card--front" aria-label="Frente do cartão">
  <div class="front__top"></div>
  <div class="front__stripe"><span class="s-teal"></span><span class="s-yellow"></span><span class="s-red"></span><span class="s-purple"></span></div>
  <div class="front__bottom">
    <ul class="contacts">
      <li><svg viewBox="0 0 16 16"><path fill="#f2f2f2" d="M4 1h3l1 4-2 1c1 2 2 3 4 4l1-2 4 1v3c0 1-1 2-2 2C6 14 2 10 2 3c0-1 1-2 2-2z"/></svg>+351 21 584 62 07</li>
      <li><svg viewBox="0 0 16 16"><rect x="4" y="1" width="8" height="14" rx="1.5" fill="none" stroke="#f2f2f2" stroke-width="1.6"/><circle cx="8" cy="12.5" r="1" fill="#f2f2f2"/></svg>+351 96 731 84 25</li>
      <li><svg viewBox="0 0 16 16"><rect x="1" y="3" width="14" height="10" fill="none" stroke="#f2f2f2" stroke-width="1.6"/><path d="M1 3l7 6 7-6" fill="none" stroke="#f2f2f2" stroke-width="1.6"/></svg>geral@velado.pt</li>
      <li><svg viewBox="0 0 16 16"><circle cx="8" cy="8" r="6.5" fill="none" stroke="#f2f2f2" stroke-width="1.6"/><path d="M1.5 8h13M8 1.5c-3 3-3 10 0 13M8 1.5c3 3 3 10 0 13" fill="none" stroke="#f2f2f2" stroke-width="1.2"/></svg>www.velado.pt</li>
      <li><svg viewBox="0 0 16 16"><rect x="1.5" y="1.5" width="13" height="13" rx="2" fill="#f2f2f2"/></svg>ninhodeluz</li>
    </ul>
    <p class="address">Rua Henrique Lobato<br>Farinha 9C<br>ZipCode: 2741-318 Quinta<br>do Orvalho</p>
  </div>

  <div class="brand">
    <span class="brand__dot"></span>
    <span class="brand__name">Ninho de Luz</span>
  </div>

  <div class="person">
    <p class="person__name">Rui Matos</p>
    <p class="person__role">President</p>
  </div>
</section>

<section class="card card--back" aria-label="Verso do cartão">
  <div class="back__brand">
    <span class="back__dot"></span>
    <span class="back__name">Ninho de Luz</span>
  </div>
  <p class="slogan">Plantamos carinho, cuidamos sorrisos, celebramos conquistas</p>
</section>

</body>
</html>
```